Flyer für Beratung rund um den Computer
Zielgruppe
Hauptsächlich: Beratung rund um den Computer, individuelle Schulungen, technische Hilfe . Aber auch: Einführung in die Programmierung, Webseitenerstellung etc. Zielgruppe sind Privatpersonen, gerne auch ältere Personen, alle die sich unsicher im Umgang mit Computern fühlen und freundliche, geduldige Hilfe suchen.
Aufgabenstellung
Da meine Zielgruppe eher keine Computerfreaks sind, sollte der Flyer nicht zu technisch aussehen, sondern für Hilfesuchende ansprechend und freundlich wirken.

```html
<!DOCTYPE html>
<html lang="de">
<head>
<meta charset="utf-8">
<title>PC ganz leicht – Flyer</title>
<link href="https://fonts.googleapis.com/css2?family=Poppins:wght@400;600;700&display=swap" rel="stylesheet">
<style>
  :root{
    --navy:#213a80;
    --navy-deep:#1c2f6e;
    --blue:#0a86c6;
    --sky:#bde4f0;
    --ice:#8fd0e6;
    --ink:#1d1d1d;
    --page:#ffffff;
    --backdrop:#eceae6;
  }
  *{margin:0;padding:0;box-sizing:border-box}
  html,body{width:1200px;height:1117px;overflow:hidden}
  body{background:var(--backdrop);font-family:"Poppins",sans-serif;color:var(--ink);position:relative}
  .flyer{position:absolute;left:220px;top:20px;width:760px;height:1076px;background:var(--page);overflow:hidden}
  .abs{position:absolute}
  .header{left:0;top:0;width:760px;height:220px}
  .brand{left:38px;top:48px;width:190px;height:124px;display:flex;align-items:center;gap:10px}
  .brand-dot{width:22px;height:22px;border-radius:50%;border:2.5px solid var(--ice);flex:none}
  .brand-name{font-weight:600;font-size:21px;line-height:1.15;color:var(--ice);letter-spacing:1px}
  .headline{left:0;width:760px;top:245px;text-align:center;font-weight:700;font-size:27.5px;color:var(--navy);letter-spacing:-.2px}
  .headline .accent{color:var(--blue)}
  .intro{left:70px;width:620px;top:284px;text-align:center;font-size:14.3px;line-height:17.5px}
  .question-box{left:56px;top:385px;width:649px;height:283px;border-radius:18px;background:linear-gradient(160deg,var(--navy-deep),var(--navy) 60%,#23449a)}
  .question-title{left:85px;top:404px;width:300px;font-weight:700;font-size:15.5px;line-height:19px;color:var(--ice)}
  .question-list{left:85px;top:452px;width:305px;list-style:none;color:#fff;font-size:13.2px;line-height:14.6px}
  .question-list li{position:relative;padding-left:21px;margin-bottom:14.5px}
  .tick{position:absolute;left:0;top:1px;width:13px;height:12px}
  .question-cta{left:56px;width:649px;top:630px;text-align:center;font-weight:700;font-size:15.5px;color:#fff}
  .photo-frame{left:388px;top:361px;width:338px;height:250px;border-radius:22px;background:var(--page)}
  .photo{left:394px;top:367px;width:326px;height:238px;border-radius:18px;background:linear-gradient(135deg,#d9d6d0,#b4866f 40%,#e3cbbd 70%,#cfd3d8)}
  .more{left:70px;width:620px;top:684px;text-align:center;font-size:14.3px;line-height:17.5px}
  .label{height:28px;display:flex;align-items:center;justify-content:center;font-weight:700;font-size:15.5px;color:#fff;background:var(--blue);clip-path:polygon(6px 0,100% 0,calc(100% - 6px) 100%,0 100%)}
  .list{list-style:none;font-size:13.2px;line-height:16.8px}
  .list li{position:relative;padding-left:19px}
  .list .tick{top:2px}
  .footer-left{left:0;top:993px;width:405px;height:83px;background:var(--blue);clip-path:polygon(0 0,100% 0,93% 100%,0 100%)}
  .footer-right{left:383px;top:993px;width:377px;height:83px;background:var(--sky);clip-path:polygon(7% 0,100% 0,100% 100%,0 100%)}
  .phone{left:58px;top:1012px;display:flex;align-items:center;gap:10px;font-weight:700;font-size:36px;color:#fff;line-height:44px}
  .contact{left:424px;top:1016px;font-weight:700;font-size:13.5px;color:var(--navy);line-height:19px}
  .contact div{display:flex;align-items:center;gap:7px}
  .contact i{width:11px;height:11px;border-radius:50%;background:var(--navy);display:inline-block}
</style>
</head>
<body>
<svg width="0" height="0" style="position:absolute">
  <defs>
    <symbol id="tick" viewBox="0 0 13 12"><path d="M1 6.5 4.8 10 12 1.5" fill="none" stroke="currentColor" stroke-width="2.6" stroke-linecap="round" stroke-linejoin="round"/></symbol>
  </defs>
</svg>

<main class="flyer">
  <svg class="abs header" viewBox="0 0 760 220">
    <polygon points="0,0 281,0 219,220 0,220" fill="#213a80"/>
    <polygon points="289,0 740,0 686,220 227,220" fill="#c9a98a"/>
    <rect role="img" aria-label="Foto: Team bespricht Webseiten-Entwürfe an einem Bildschirm" x="0" y="0" width="0" height="0"/>
    <polygon points="760,30 760,195 708,195" fill="#0a86c6"/>
  </svg>
  <div class="abs" role="img" aria-label="Foto: Team bespricht Webseiten-Entwürfe an einem Bildschirm" style="left:289px;top:0;width:420px;height:220px;clip-path:polygon(0 0,451px 0,397px 220px,-62px 220px);background:linear-gradient(120deg,#e8e4de,#c79a78 45%,#e6e2dc 80%)"></div>

  <div class="abs brand"><span class="brand-dot"></span><span class="brand-name">PC GANZ<br>LEICHT</span></div>

  <h1 class="abs headline"><span class="accent">COMPUTER –</span> ALLES, NUR KEIN HEXENWISSEN</h1>
  <p class="abs intro">Ganz egal, was Sie im Zusammenhang mit Ihrem Rechner umtreibt - ob Sie sich manchmal einfach etwas unsicher fühlen, mit einer Anwendung nicht zurecht kommen oder Ihr Rechner nicht so reagiert, wie er sollte - mein Ziel ist es, dass Sie sich im Umgang mit Ihrem Computer sicher fühlen und Freude daran haben.</p>

  <div class="abs question-box"></div>
  <h2 class="abs question-title">Auch viele andere Themen werfen immer wieder Fragen auf:</h2>
  <ul class="abs question-list" style="color:#fff">
    <li><svg class="tick" style="color:var(--ice)"><use href="#tick"/></svg>Ich brauche einen neuen Rechner - wie finde ich heraus, was ich wirklich brauche?</li>
    <li><svg class="tick" style="color:var(--ice)"><use href="#tick"/></svg>Wie organisiere ich meinen Rechner damit ich alles schnell wiederfinde?</li>
    <li><svg class="tick" style="color:var(--ice)"><use href="#tick"/></svg>Wie bekomme ich die Fotos von meiner Kamera / meinem Smartphone auf meinen Rechner?</li>
    <li><svg class="tick" style="color:var(--ice)"><use href="#tick"/></svg>...und so weiter.</li>
  </ul>
  <p class="abs question-cta">Legen Sie los - egal wie klein oder groß Ihre Frage ist - ich helfe gerne!</p>

  <div class="abs photo-frame"></div>
  <div class="abs photo" role="img" aria-label="Foto: Paar sitzt lächelnd vor einem Laptop in der Küche"></div>

  <p class="abs more">Und für alle, die etwas mehr wissen wollen - z.B. wie das mit dem Programmieren eigentlich funktioniert, wie eine Webseite entsteht, wofür ein Router benötigt wird, wie nutze ich eine KI, usw. - ich gebe gerne eine Einführung dazu.</p>

  <div class="abs label" style="left:65px;top:754px;width:300px">Beratung rund um Ihren Rechner:</div>
  <ul class="abs list" style="left:85px;top:792px">
    <li><svg class="tick"><use href="#tick"/></svg>Kauf</li>
    <li><svg class="tick"><use href="#tick"/></svg>Organisation</li>
    <li><svg class="tick"><use href="#tick"/></svg>Anwendungen</li>
    <li><svg class="tick"><use href="#tick"/></svg>Optimierung</li>
  </ul>
  <ul class="abs list" style="left:218px;top:792px">
    <li><svg class="tick"><use href="#tick"/></svg>Internet</li>
    <li><svg class="tick"><use href="#tick"/></svg>Datensicherung</li>
    <li><svg class="tick"><use href="#tick"/></svg>... und vieles mehr</li>
  </ul>

  <div class="abs label" style="left:65px;top:868px;width:300px">Für alle, die mehr wollen:</div>
  <ul class="abs list" style="left:85px;top:906px">
    <li><svg class="tick"><use href="#tick"/></svg>Einführung in die Programmierung</li>
    <li><svg class="tick"><use href="#tick"/></svg>Erstellen einer Website</li>
    <li><svg class="tick"><use href="#tick"/></svg>Wie komme ich einer KI näher?</li>
    <li><svg class="tick"><use href="#tick"/></svg>oder: was interessiert Sie?</li>
  </ul>

  <div class="abs label" style="left:394px;top:754px;width:300px">Technische Hilfe:</div>
  <ul class="abs list" style="left:403px;top:793px;width:260px">
    <li><svg class="tick"><use href="#tick"/></svg>Anschluß von Peripheriegeräten</li>
    <li><svg class="tick"><use href="#tick"/></svg>Einbinden von Peripheriegeräten ins Netzwerk / WLAN</li>
    <li><svg class="tick"><use href="#tick"/></svg>Kleinere Reparaturen</li>
    <li><svg class="tick"><use href="#tick"/></svg>oder: was brauchen Sie?</li>
  </ul>

  <div class="abs label" style="left:394px;top:886px;width:300px">Individuelle Schulungen:</div>
  <ul class="abs list" style="left:403px;top:923px">
    <li><svg class="tick"><use href="#tick"/></svg>allgemeiner Umgang mit dem Rechner</li>
    <li><svg class="tick"><use href="#tick"/></svg>Nutzung bestimmter Anwendungen</li>
    <li><svg class="tick"><use href="#tick"/></svg>oder: was wünschen Sie sich?</li>
  </ul>

  <div class="abs footer-left"></div>
  <div class="abs footer-right"></div>
  <div class="abs phone">
    <svg width="30" height="30" viewBox="0 0 30 30"><circle cx="15" cy="15" r="15" fill="#fff"/><path d="M10.2 7.5c.6-.4 1.4-.3 1.8.3l1.6 2.5c.4.6.3 1.3-.2 1.8l-1 .9c.8 1.9 2.3 3.5 4.3 4.5l.9-1c.5-.5 1.2-.6 1.8-.2l2.5 1.5c.6.4.8 1.2.4 1.8l-.9 1.4c-.6 1-1.8 1.4-2.9 1-5-1.7-8.6-5.4-10.2-10.3-.3-1.1.1-2.3 1-2.9z" fill="#0a86c6"/></svg>
    0170 555 0192
  </div>
  <div class="abs contact">
    <div><i></i>lena@pc-ganz-leicht.de</div>
    <div><i></i>www.pc-ganz-leicht.de</div>
  </div>
</main>
</body>
</html>
```